" ATENDEMOS CLIENTES DE BALCÃO PARA VENDA DE PEÇAS E PNEUS DA LINHA LEVE + CAMIONETES NACIONAIS E IMPORTADOS. CONTAMOS COM UM CENTRO AUTOMOTIVO DE GRANDE PORTE PARA EXECUTAR SERVIÇOS MECÂNICOS DE REVISÃO E MANUTENÇÃO CORRETIVA E PREVENTIVA ( ALINHAMENTO, BALANCEAMENTO, MONTAGEM DE PNEUS, SUSPENSÃO, FREIOS, CAMBIO MANUAL E AUTOMATIZADO, INJEÇÃO ELETRÔNICA, REPARO DE MOTOR E CABEÇOTES, SISTEMA DE DIREÇÃO ). "

```html
<!DOCTYPE html>
<html lang="pt-BR">
<head>
<meta charset="UTF-8">
<title>KV Auto — Adesivo</title>
<link href="https://fonts.googleapis.com/css2?family=Montserrat:wght@500;600;800&display=swap" rel="stylesheet">
<style>
  :root {
    --backdrop: #1c232b;
    --sticker: #ffffff;
    --brand-red: #e1262b;
    --ink-dark: #1f2a36;
    --ink-grey: #7a8088;
  }
  html, body {
    margin: 0;
    width: 1200px;
    height: 1200px;
    overflow: hidden;
    background: var(--backdrop);
    font-family: "Montserrat", sans-serif;
  }
  .sticker {
    position: absolute;
    left: 100px;
    top: 100px;
    width: 1000px;
    height: 1000px;
  }
  .sticker-shape {
    position: absolute;
    inset: 0;
  }
  .brand {
    position: absolute;
    left: 0;
    right: 0;
    top: 330px;
    text-align: center;
  }
  .brand-name {
    margin: 0;
    font-weight: 800;
    font-size: 150px;
    line-height: 1;
    letter-spacing: -2px;
    color: var(--ink-dark);
  }
  .brand-tagline {
    margin: 14px 0 0;
    font-weight: 600;
    font-size: 30px;
    letter-spacing: 8px;
    color: var(--ink-grey);
  }
  .contact {
    position: absolute;
    left: 0;
    right: 0;
    top: 600px;
    text-align: center;
    color: var(--ink-dark);
  }
  .contact-phone {
    margin: 0;
    font-weight: 500;
    font-size: 46px;
  }
  .contact-site {
    margin: 14px 0 0;
    font-weight: 600;
    font-size: 40px;
    letter-spacing: 12px;
  }
  .contact-site .highlight { color: var(--brand-red); }
</style>
</head>
<body>
  <div class="sticker">
    <svg class="sticker-shape" viewBox="0 0 1000 1000" aria-hidden="true">
      <circle cx="500" cy="500" r="500" fill="var(--sticker)"/>
      <path d="M72.4 655.6 A455 455 0 0 1 894 272.5" fill="none" stroke="var(--brand-red)" stroke-width="13"/>
      <path d="M953.3 460.3 A455 455 0 0 1 178.3 821.7" fill="none" stroke="var(--ink-dark)" stroke-width="13"/>
    </svg>
    <div class="brand">
      <p class="brand-name">KV AUTO</p>
      <p class="brand-tagline">PNEUS · PEÇAS · SERVIÇOS</p>
    </div>
    <div class="contact">
      <p class="contact-phone">99 9999-999</p>
      <p class="contact-site">www.<span class="highlight">site</span>.com.br</p>
    </div>
  </div>
</body>
</html>
```